Book Cover (QUIET WEEKS MEND EVERY KNOT)

This book is a series of blog posts from my blog, Sparks Kept Handy, which is at glenferrante.example/blog.
The book is to be called:
QUIET WEEKS MEND EVERY KNOT
And 51 other Sparks Kept Handy from the Corner Shop Tutor
(Sparks Kept Handy) should be italicized.
My name is Glen Ferrante, M.B.A.

I will need three variations for my paperback, hardcover and e-book.
Here are some of the blog titles and their topics:
Preparing Your Small Business For Recession small business recession
Should I Incorporate My Business? Should I Incorporate My Business?
Alternative to Minority Shareholder In Small Private Companies minority shareholder
Small Business Culture – Getting it Right Small Business Culture
What is The Right Way to Fire Someone The Right Way to Fire Someone
The Five Basic Leadership Principles Leadership Principles
10 Tips for New Entrepreneurs – Sure Ways to Increase Your Chances of Success
10 things to consider before becoming an entrepreneur
Strategy vs Biz Plans small business strategy
Closing Sales close the sale
Breakeven break even
Growth makes cash flow suck cash flow issues
Think Twice About Offering Early Payment Discounts prepayment discounts
Firing Customers firing customers
Collections best practices getting paid faster
The Cash Flow Statement cash flow statement
Using Paralegals paralegal
Radical Candor radical candor
Why No is the Second Best Word to a Salesperson's ears value of no
The $8 Million Problem -
Contractor vs Employee contractor vs employee
The Columbo sales tactic
Systems Turn Goals From Dreams Into Reality Systems vs Goals
The Importance of Realistic Goals stretch goals
Why The Owner Must Review Every Hire hiring for values
Systems Thinking for Small Biz: The Case for SOPs systems thinking
Trust Your Gut business intuition
Grease and friction grease vs friction
Left alone, 90% of problems solve themselves strategic inaction
Referrals Are Great—But Not a Growth Strategy referrals
The Lean Marketing Machine: 7 Hacks to Grow Your Small Business Fast marketing hacks
The Small Business Health Check small business health check
How to Spot a Customer Headed for Trouble — Before They Take You Down With Them customer warning signs
We Are What We Repeatedly Do habits
The Smartest People Know When to Play Dumb playing dumb
Before You Scale, Do the Math unit economics
AI for Small Business: Practical Tools and Use Cases AI for Small Business
Title: Tell Me Right Now—Why Can’t We Raise Your Prices? small business pricing
Why Your Real Competitor Isn’t Who You Think creative destruction
Good Enough Might Be Great satisficing
Bootstrapping: Building Your Business on Your Terms bootstrapping
Building Resilient Companies That Never Have to Bet the Farm bet the farm
We Always Overshoot: From Fiber to Cannabis to AI AI overbuild
A Bias Toward Action bias toward ation
Choosing the Right Business Owner Title business owner title
Jobs to Be Done: Understanding What Your Customers Really Want Jobs to Be Done
Forget Money. Here’s What Really Motivates People. motivation

Target Market(s)

Small business operators, business school students

Industry/Entity Type

Small business

Colors

Designer to choose colors to be used in the design.

Requirements
Should not have
• Should not look cartoonish

```html
<!DOCTYPE html>
<html lang="en">
<head>
<meta charset="utf-8">
<title>Quiet Weeks Mend Every Knot — Book Cover</title>
<link href="https://fonts.googleapis.com/css2?family=Bebas+Neue&family=PT+Serif:ital,wght@1,400;1,700&family=Montserrat:wght@500&display=swap" rel="stylesheet">
<style>
  :root {
    --backdrop: #808085;
    --paper: #f4f4f4;
    --paper-shade: #e6e7e8;
    --navy: #00233f;
    --slate: #263a4c;
    --stone: #3b4551;
    --sand: #ecebe8;
  }
  * { margin: 0; padding: 0; box-sizing: border-box; }
  html, body {
    width: 1200px; height: 1200px; overflow: hidden;
    background: var(--backdrop);
  }
  .cover {
    position: absolute;
    left: 221px; top: 31px;
    width: 758px; height: 1137px;
    background: linear-gradient(180deg, var(--paper) 0%, var(--paper) 50%, var(--paper-shade) 56%, var(--paper) 66%, var(--paper) 88%, var(--paper-shade) 100%);
    overflow: hidden;
  }
  .title-rule-row {
    position: absolute;
    left: 57px; width: 640px;
    display: flex; align-items: center; gap: 18px;
  }
  .title-rule-row .rule {
    flex: 1; height: 2px; background: var(--slate);
  }
  .title-small {
    font-family: "PT Serif", serif;
    font-style: italic; font-weight: 400;
    font-size: 92px; line-height: 1;
    color: var(--slate);
    letter-spacing: 1px;
    white-space: nowrap;
  }
  .row-one { top: 72px; }
  .row-three { top: 320px; }
  .title-big {
    position: absolute;
    left: 0; width: 100%;
    text-align: center;
    font-family: "Bebas Neue", sans-serif;
    font-weight: 400;
    color: var(--navy);
    line-height: 1;
    white-space: nowrap;
  }
  .big-one { top: 180px; font-size: 160px; }
  .big-two { top: 407px; font-size: 166px; letter-spacing: 2px; }
  .subtitle {
    position: absolute;
    right: 58px; top: 608px;
    text-align: right;
    font-family: "PT Serif", serif;
    font-style: italic; font-weight: 700;
    font-size: 37px; line-height: 45px;
    color: var(--slate);
    letter-spacing: 1px;
  }
  .subtitle em { font-style: italic; }
  .stones-image {
    position: absolute;
    left: 102px; top: 671px;
    width: 627px; height: 304px;
    background:
      radial-gradient(ellipse 110px 150px at 115px 190px, var(--stone) 0%, var(--stone) 70%, rgba(59,69,81,0) 100%),
      radial-gradient(ellipse 200px 70px at 420px 250px, var(--sand) 0%, rgba(236,235,232,0) 100%);
  }
  .author {
    position: absolute;
    left: 0; width: 100%; top: 1038px;
    text-align: center;
    font-family: "Montserrat", sans-serif;
    font-weight: 500;
    font-size: 49px;
    color: var(--slate);
    letter-spacing: 0.5px;
    white-space: nowrap;
  }
</style>
</head>
<body>
  <main class="cover">
    <h1 class="book-title">
      <span class="title-rule-row row-one">
        <span class="rule"></span>
        <span class="title-small">QUIET</span>
        <span class="rule"></span>
      </span>
      <span class="title-big big-one">WEEKS MEND</span>
      <span class="title-rule-row row-three">
        <span class="rule"></span>
        <span class="title-small">EVERY</span>
        <span class="rule"></span>
      </span>
      <span class="title-big big-two">KNOT</span>
    </h1>

    <p class="subtitle">And 51 Other <em>Sparks</em><br><em>Kept Handy</em> from<br>the Corner Shop<br>Tutor</p>

    <div class="stones-image" role="img" aria-label="Photograph of a balanced stack of smooth dark stones beside a small mound of white sand"></div>

    <p class="author">GLEN FERRANTE, M.B.A.</p>
  </main>
</body>
</html>
```